CrashPals Personal Injury Lawyers Website (Wordpress)

We need a brand new website for our firm's new rebranding. The name of the website is www.crashpals-example.com. Our new brand will be a group of personal injury lawyers focused on representing only victims in car wrecks. We will be distinguishing ourselves from other law firms due to the fact that other law firms represent clients involving all forms of personal injury. We will only focus on car wrecks and this needs to be reflected on the website.

I have attached the new firm logo and stationary to show the designers the kind of look we are going for in the new website. It needs to be clean, pure, and show the potential clients that we only do one thing and we do it well. That thing is car wrecks.

Some examples of websites that we like are the following:
www.qtr-example.lu - nice interface and colors. nice navigation, we really like the biography pages for the individuals attorneys
www.harlowpinelegal-example.com - good layout, good navigation
www.maddoxtrevane-example.com - navigation bar follows the user whether the user goes up or down

We would like five separate pages -- (1) Home, (2) Client Resources, (3) Expertise / Car Wrecks, (4) Contact Us, (5) News

The Home page will be used for driving traffic and should have a call to action on the right at the top stating that we will send an ebook to anyone who gives their contact information. The ebook will explain how car wrecks work. This should also have room for youtube videos which will be added later.

The client resources will include blogs, books, and information for potential clients. It should be presented in a well developed manner which is both appealing to potential and current clients.

The expertise page will show that we only focus on car wrecks. This needs to be a recurrent theme throughout the entire website. This page will focus on car wrecks and the different aspects including damages, insurance, and investigation.

The Contact Us page will show a google map to our address and phone number. Please use generic information and we will fill in the gaps upon the selection.

News: the news page will show different articles related to past and present cases and the successes of those clients.

The overall page should be elegant and creative. Do not include courthouses, gavels or anything else related to the law. If you include these things, your design will automatically be excluded.
Updates

Please take note this design is now guaranteed. I look forward to receiving everyone's wonderful designs.

Target Market(s)

Persons involved in car wrecks

Industry/Entity Type

Legal

Coding

Coded - Design and coding required

Number of Pages Required

5+ page

Font styles to use
Serif
Sans Serif

Colors
ec1f27
ffffff
000000

Requirements
Must have
• Five pages which focus on representation of car wreck victims. The site must be clean and easy to navigate.
Nice to have
• Navigation bar should follow user up and down the page.
Should not have
• Gavels, court houses, anything related to the law. If your design has these aspects, it will automatically be rejected

```html
<!DOCTYPE html>
<html lang="en">
<head>
<meta charset="utf-8">
<title>CrashPals – Personal Injury Lawyers</title>
<link rel="stylesheet" href="https://fonts.googleapis.com/css2?family=Open+Sans:wght@400;600;700;800&family=Roboto+Slab:wght@400;700&display=swap">
<style>
:root{
  --red:#ec1f27;
  --red-dark:#c3161d;
  --ink:#1e1e1e;
  --text:#5a5a5a;
  --muted:#8a8a8a;
  --line:#e2e2e2;
  --nav:#2b2b2b;
  --dark:#262626;
  --footer:#2f2f2f;
  --gold:#b8912f;
  --white:#ffffff;
}
*{box-sizing:border-box;margin:0;padding:0}
html,body{width:1200px;height:2568px;overflow:hidden}
body{font-family:"Open Sans",Arial,sans-serif;color:var(--text);background:var(--white);font-size:13px;line-height:1.6}
.page{width:1200px;height:2568px;position:relative}
.wrap{width:1080px;margin:0 auto;position:relative}

/* header */
.site-header{height:100px}
.site-header .wrap{display:flex;justify-content:space-between;align-items:center;height:100px}
.brand{display:flex;align-items:center;gap:12px}
.brand-mark{width:22px;height:22px;background:var(--red)}
.brand-name{font-size:36px;font-weight:700;color:var(--ink);line-height:1}
.call{display:flex;align-items:center;gap:12px}
.call-icon{width:42px;height:42px;border-radius:50%;background:var(--red);display:flex;align-items:center;justify-content:center}
.call small{display:block;font-size:12px;color:var(--muted)}
.call strong{display:block;font-size:22px;color:var(--red);font-weight:700;line-height:1.1}

/* nav */
.main-nav{height:36px;background:var(--nav)}
.main-nav .wrap{display:flex;justify-content:space-between;height:36px}
.main-nav ul{list-style:none;display:flex}
.main-nav li{color:#ddd;font-size:12px;font-weight:600;padding:0 22px;line-height:36px;letter-spacing:.5px}
.main-nav li.active{background:var(--red);color:var(--white)}
.nav-cta{background:#1a1a1a;color:var(--white);font-size:12px;font-weight:700;padding:0 24px;line-height:33px;letter-spacing:.5px;border-top:3px solid var(--red)}

/* hero */
.hero{height:334px;position:relative;background:linear-gradient(120deg,#5d6468 0%,#8c9397 35%,#4a4f52 70%,#2f3336 100%)}
.hero-copy{position:absolute;left:60px;bottom:40px;width:620px}
.hero-copy h1{background:rgba(20,20,20,.75);color:var(--white);font-size:30px;font-weight:700;line-height:1.25;padding:16px 22px}
.hero-copy p{background:var(--red);color:var(--white);font-size:15px;padding:8px 22px}

/* welcome */
.welcome{height:470px;padding-top:50px}
.welcome .wrap{display:flex;gap:50px}
.welcome-text{width:530px}
.section-title{font-size:26px;font-weight:800;color:var(--ink);letter-spacing:.5px;line-height:1.2}
.section-title em{font-style:normal;color:var(--red)}
.title-rule{width:60px;height:3px;background:var(--red);margin:10px 0 18px}
.welcome-text p{margin-bottom:14px}
.btn-outline{display:inline-block;border:1px solid var(--red);color:var(--red);font-size:11px;font-weight:700;padding:4px 12px;margin-top:6px}
.video{width:500px;height:290px;background:linear-gradient(135deg,#3b3b3b,#6e6e6e 55%,#242424);position:relative;display:flex;align-items:center;justify-content:center}
.video-caption{width:500px;font-size:12px;color:var(--muted);margin-top:12px}

/* expertise */
.expertise{height:340px;display:flex}
.expertise-intro{width:600px;padding:60px 60px;color:var(--white);background:linear-gradient(135deg,rgba(236,31,39,.92),rgba(170,18,24,.95)),linear-gradient(90deg,#555,#222)}
.expertise-intro h2{font-size:26px;font-weight:800;letter-spacing:.5px;margin-bottom:14px}
.expertise-intro p{font-size:14px;line-height:1.65;margin-bottom:18px;opacity:.95}
.btn-white{display:inline-block;border:1px solid var(--white);color:var(--white);font-size:11px;font-weight:700;padding:4px 12px}
.expertise-list{width:600px;background:var(--dark);padding:36px 60px;list-style:none}
.expertise-list li{display:flex;gap:20px;margin-bottom:24px;color:#bdbdbd}
.expertise-list .icon{flex:0 0 56px;height:56px;border-radius:50%;border:2px solid var(--white);display:flex;align-items:center;justify-content:center}
.expertise-list h3{color:var(--white);font-size:15px;font-weight:700;letter-spacing:1px}
.expertise-list p{font-size:12px;line-height:1.5}

/* ebook */
.ebook{height:280px;padding-top:40px}
.ebook .wrap{display:flex;justify-content:space-between;align-items:flex-start}
.ebook-copy{padding-top:16px}
.ebook-copy .kicker{font-size:22px;color:var(--red);font-weight:600}
.ebook-copy h2{font-size:36px;font-weight:800;color:var(--ink);line-height:1.15;margin:10px 0 18px}
.btn-red{display:inline-block;background:var(--red);color:var(--white);font-size:13px;font-weight:700;padding:10px 20px}
.ebook-frame{width:440px;height:210px;background:#161616;border-radius:10px;padding:12px}
.ebook-panel{height:100%;background:linear-gradient(135deg,#c9a23f,var(--gold) 60%,#9a7822);padding:18px 26px;color:var(--white)}
.ebook-panel .kicker{font-size:13px}
.ebook-panel h3{font-size:22px;font-weight:800;line-height:1.2;margin:8px 0 14px}
.btn-black{display:inline-block;background:#111;color:var(--white);font-size:11px;font-weight:700;padding:7px 14px}

/* news */
.news{height:340px;padding-top:20px}
.heading-rule{display:flex;align-items:center;gap:20px;justify-content:center;margin-bottom:30px}
.heading-rule::before,.heading-rule::after{content:"";height:1px;width:380px;background:var(--line)}
.news-grid{display:flex;gap:30px}
.news-card{flex:1;border:1px solid var(--line);padding:18px;display:flex;gap:16px;height:170px}
.date{flex:0 0 60px;height:62px;background:var(--dark);color:var(--white);text-align:center}
.date b{display:block;font-size:24px;line-height:40px}
.date span{display:block;background:var(--red);font-size:11px;font-weight:700;line-height:22px}
.news-card h3{color:var(--red);font-size:13px;font-weight:700;line-height:1.4;margin-bottom:8px}
.news-card p{font-size:12px;line-height:1.55}

/* posts + testimonials */
.feature{height:358px;padding-top:10px}
.feature .wrap{display:flex;gap:60px}
.feature-col{flex:1}
.col-head{display:flex;justify-content:space-between;align-items:center;border-bottom:2px solid var(--line);padding-bottom:10px;margin-bottom:20px;position:relative}
.col-head::after{content:"";position:absolute;left:0;bottom:-2px;width:110px;height:2px;background:var(--red)}
.col-head h2{font-size:22px;font-weight:800;color:var(--ink)}
.col-head h2 em{font-style:normal;color:var(--red)}
.view-all{font-size:10px;border:1px solid var(--line);padding:2px 8px;color:var(--muted)}
.post{display:flex;gap:16px;margin-bottom:22px}
.post-thumb{flex:0 0 120px;height:84px;background:linear-gradient(135deg,#2f4e78,#8aa1b8)}
.post h3{color:var(--red);font-size:13px;font-weight:700}
.post .meta{font-size:11px;color:var(--muted);margin:2px 0 4px}
.post p{font-size:12px;line-height:1.5}
.testimonial{display:flex;gap:20px}
.portrait{flex:0 0 90px;height:90px;border-radius:50%;background:linear-gradient(135deg,#c7b3a0,#6b5d52)}
.testimonial blockquote{font-family:"Roboto Slab",Georgia,serif;font-size:14px;line-height:1.7;color:var(--text)}
.testimonial cite{display:block;margin-top:14px;font-style:normal;font-size:12px;color:var(--muted)}

/* footer */
.site-footer{height:318px;background:var(--footer);color:#bdbdbd;padding-top:36px}
.footer-cols{display:flex;gap:60px;height:220px}
.footer-col{flex:1}
.footer-col h4{color:var(--white);font-size:14px;font-weight:700;letter-spacing:1px;margin-bottom:16px}
.field{height:26px;background:var(--white);margin-bottom:8px;font-size:11px;color:#999;padding:4px 8px}
.field.tall{height:44px}
.footer-btn{display:inline-block;background:var(--white);color:var(--ink);font-size:11px;font-weight:700;padding:3px 12px}
.signup{display:flex;margin-top:14px}
.signup .field{flex:1;margin:0}
.signup span{background:var(--red);color:var(--white);font-size:11px;font-weight:700;padding:4px 14px;height:26px}
.find li{list-style:none;display:flex;gap:12px;margin-bottom:14px;font-size:12px;align-items:flex-start}
.find svg{flex:0 0 18px;margin-top:2px}
.footer-bar{border-top:1px solid #444;display:flex;justify-content:space-between;align-items:center;padding-top:14px}
.follow{display:flex;align-items:center;gap:10px;color:var(--white);font-weight:700;font-size:13px;letter-spacing:1px}
.follow i{width:26px;height:26px;border-radius:50%;background:#555;display:inline-block}
.copyright{font-size:11px;color:#999}
</style>
</head>
<body>
<div class="page">

<header class="site-header">
  <div class="wrap">
    <div class="brand">
      <span class="brand-mark"></span>
      <span class="brand-name">CrashPals</span>
    </div>
    <div class="call">
      <div class="call-icon">
        <svg width="20" height="20" viewBox="0 0 24 24"><path fill="#fff" d="M6.6 10.8a15.1 15.1 0 0 0 6.6 6.6l2.2-2.2c.3-.3.7-.4 1-.2 1.1.4 2.3.6 3.6.6.6 0 1 .4 1 1V20c0 .6-.4 1-1 1A17 17 0 0 1 3 4c0-.6.4-1 1-1h3.5c.6 0 1 .4 1 1 0 1.3.2 2.5.6 3.6.1.3 0 .7-.2 1z"/></svg>
      </div>
      <div><small>Call Today</small><strong>123-456-7890</strong></div>
    </div>
  </div>
</header>

<nav class="main-nav">
  <div class="wrap">
    <ul>
      <li class="active">HOME</li>
      <li>CLIENT RESOURCES</li>
      <li>EXPERTISE / CAR WRECKS</li>
      <li>NEWS</li>
      <li>CONTACT US</li>
    </ul>
    <div class="nav-cta">HOW CAR WRECKS WORK ▾</div>
  </div>
</nav>

<section class="hero" role="img" aria-label="Photo of two damaged cars after a road collision">
  <div class="hero-copy">
    <h1>We understand the stress<br>your disability causes.</h1>
    <p>We know that you need your benefits as soon as possible.</p>
  </div>
</section>

<section class="welcome">
  <div class="wrap">
    <div class="welcome-text">
      <h2 class="section-title">WELCOME TO CRASHPALS</h2>
      <div class="title-rule"></div>
      <p>We represent one kind of client only: people hurt in car wrecks. Every case we take is a crash case, and every lawyer on our team spends each day on crash claims, crash evidence and crash insurers. That focus lets us move faster and argue harder for you.</p>
      <p>From the first call we gather police reports, photos, medical records and witness accounts so nothing is missed. We deal with the adjusters, so you can rest, heal and get back on the road.</p>
      <p>We work on contingency, which means you pay nothing unless we win. Call today for a free, no-pressure review of your accident.</p>
      <span class="btn-outline">Read More</span>
    </div>
    <div>
      <div class="video" role="img" aria-label="Video still of a lawyer speaking with an injured client">
        <svg width="74" height="74" viewBox="0 0 74 74"><circle cx="37" cy="37" r="36" fill="#ec1f27"/><path d="M30 24 L52 37 L30 50 Z" fill="#fff"/></svg>
      </div>
      <p class="video-caption">Watch: what to do in the first hours after a car wreck.</p>
    </div>
  </div>
</section>

<section class="expertise">
  <div class="expertise-intro" role="img" aria-label="Red-toned photo of a wrecked car">
    <h2>EXPERTISE / CAR WRECKS</h2>
    <p>Car wrecks are all we do. We know how crashes happen, how injuries are proven and how insurers try to pay less. We use that knowledge to build a claim that is clear, strong and ready for court.</p>
    <span class="btn-white">Read More</span>
  </div>
  <ul class="expertise-list">
    <li>
      <span class="icon"><svg width="26" height="26" viewBox="0 0 24 24"><text x="12" y="18" text-anchor="middle" font-family="Open Sans,sans-serif" font-size="18" font-weight="700" fill="#fff">$</text></svg></span>
      <div><h3>DAMAGES</h3><p>Medical bills, lost wages, pain and car repair. We count every loss so your claim reflects its full value.</p></div>
    </li>
    <li>
      <span class="icon"><svg width="24" height="24" viewBox="0 0 24 24"><path d="M12 2 L20 5 V11 C20 16 16.5 20 12 22 C7.5 20 4 16 4 11 V5 Z" fill="none" stroke="#fff" stroke-width="2"/></svg></span>
      <div><h3>INSURANCE</h3><p>We handle adjusters and policy limits so you never face an insurer on your own or settle for less.</p></div>
    </li>
    <li>
      <span class="icon"><svg width="24" height="24" viewBox="0 0 24 24"><circle cx="10" cy="10" r="6" fill="none" stroke="#fff" stroke-width="2"/><path d="M14.5 14.5 L20 20" stroke="#fff" stroke-width="2.5" stroke-linecap="round"/></svg></span>
      <div><h3>INVESTIGATION</h3><p>Scene photos, skid marks and witness talks. We rebuild the crash to show clearly who was at fault.</p></div>
    </li>
  </ul>
</section>

<section class="ebook">
  <div class="wrap">
    <div class="ebook-copy">
      <div class="kicker">Download our Free eBook:</div>
      <h2>A Complete Guide To<br>Personal Injury Lawyers Law</h2>
      <span class="btn-red">Download eBook Now</span>
    </div>
    <div class="ebook-frame">
      <div class="ebook-panel">
        <div class="kicker">Download our Free eBook:</div>
        <h3>A Complete Guide To<br>Personal Injury Lawyers Law</h3>
        <span class="btn-black">Download eBook Now</span>
      </div>
    </div>
  </div>
</section>

<section class="news">
  <div class="wrap">
    <h2 class="section-title heading-rule">LATEST <em>NEWS</em></h2>
    <div class="news-grid">
      <article class="news-card">
        <div class="date"><b>22</b><span>Aug</span></div>
        <div><h3>Rear-end crash victim wins full cover for surgery</h3><p>A driver hit at a red light received full payment for surgery and six months of lost pay after a short trial.</p></div>
      </article>
      <article class="news-card">
        <div class="date"><b>15</b><span>June</span></div>
        <div><h3>Highway pile-up claim settled for three families</h3><p>Our team proved the truck driver's fault and secured a fair settlement for every family hurt in the wreck.</p></div>
      </article>
      <article class="news-card">
        <div class="date"><b>10</b><span>Feb</span></div>
        <div><h3>Insurer's low offer rejected, client paid triple</h3><p>After a detailed crash study, the insurer raised its offer and our client got the care she needed.</p></div>
      </article>
    </div>
  </div>
</section>

<section class="feature">
  <div class="wrap">
    <div class="feature-col">
      <div class="col-head"><h2>LATEST <em>POST</em></h2><span class="view-all">View All</span></div>
      <div class="post">
        <div class="post-thumb" role="img" aria-label="Photo of a blue car on a city road"></div>
        <div><h3>Five steps to take right after a car wreck</h3><div class="meta">Admin · 12 Comments</div><p>Stay safe, call the police, take photos and see a doctor, even if you feel fine at first.</p></div>
      </div>
      <div class="post">
        <div class="post-thumb" role="img" aria-label="Photo of a damaged car at a crash scene"></div>
        <div><h3>Why you should not sign the first offer</h3><div class="meta">Admin · 8 Comments</div><p>Early offers rarely cover future care. Learn what to ask before you agree to any settlement.</p></div>
      </div>
    </div>
    <div class="feature-col">
      <div class="col-head"><h2>CLIENT <em>TESTIMONIALS</em></h2><span class="view-all">View All</span></div>
      <div class="testimonial">
        <div class="portrait" role="img" aria-label="Portrait photo of a satisfied client"></div>
        <div>
          <blockquote>“After my wreck I did not know where to turn. The CrashPals team took every call, explained each step and fought the insurer until I was paid in full. I could focus on healing while they handled the rest. I would trust them again without a second thought.”</blockquote>
          <cite>— Mr. Owen Calder</cite>
        </div>
      </div>
    </div>
  </div>
</section>

<footer class="site-footer">
  <div class="wrap">
    <div class="footer-cols">
      <div class="footer-col">
        <h4>QUICK CONTACT</h4>
        <div class="field">Name</div>
        <div class="field">Email</div>
        <div class="field">Phone</div>
        <div class="field tall">Message</div>
        <span class="footer-btn">Submit</span>
      </div>
      <div class="footer-col">
        <h4>NEWSLETTER SIGNUP</h4>
        <p>Get the latest crash law updates and safety tips by entering your email address below.</p>
        <div class="signup"><div class="field">Email address</div><span>Subscribe</span></div>
      </div>
      <div class="footer-col">
        <h4>FIND US</h4>
        <ul class="find">
          <li><svg width="18" height="18" viewBox="0 0 24 24"><path fill="#ec1f27" d="M12 2a7 7 0 0 0-7 7c0 5 7 13 7 13s7-8 7-13a7 7 0 0 0-7-7zm0 9.5A2.5 2.5 0 1 1 12 6.5a2.5 2.5 0 0 1 0 5z"/></svg><span>100 Main Street, Suite 200<br>Your City, ST 00000</span></li>
          <li><svg width="18" height="18" viewBox="0 0 24 24"><path fill="#ec1f27" d="M6.6 10.8a15.1 15.1 0 0 0 6.6 6.6l2.2-2.2c.3-.3.7-.4 1-.2 1.1.4 2.3.6 3.6.6.6 0 1 .4 1 1V20c0 .6-.4 1-1 1A17 17 0 0 1 3 4c0-.6.4-1 1-1h3.5c.6 0 1 .4 1 1 0 1.3.2 2.5.6 3.6.1.3 0 .7-.2 1z"/></svg><span>123-456-7890</span></li>
          <li><svg width="18" height="18" viewBox="0 0 24 24"><rect x="3" y="5" width="18" height="14" rx="1" fill="none" stroke="#ec1f27" stroke-width="2"/><path d="M3 6 L12 13 L21 6" fill="none" stroke="#ec1f27" stroke-width="2"/></svg><span>hello@crashpals-example.com</span></li>
        </ul>
      </div>
    </div>
    <div class="footer-bar">
      <div class="follow">FOLLOW US <i></i><i></i><i></i><i></i></div>
      <div class="copyright">Copyright © CrashPals. All rights reserved.</div>
    </div>
  </div>
</footer>

</div>
</body>
</html>
```